Northfield Builders Guild Business card

We are looking for a new business card design with photo included.
Our business is a nonprofit construction contractor membership organization. We offer business education, assist with business setup and licensing, provide safety training, and provide a member directory.
URL: www.brickwayguildnetwork.org
Color code:
CMYK: 0 cyan, 42 magenta, 100 yellow, 0 black for Print.
Hexidecimal: #FF9900
RGB: R 255; G 153; B 0

```html
<!DOCTYPE html>
<html lang="en">
<head>
<meta charset="utf-8">
<title>Northfield Builders Guild Business Card</title>
<link href="https://fonts.googleapis.com/css2?family=Open+Sans:wght@400;600;800&family=Orbitron:wght@500&display=swap" rel="stylesheet">
<style>
  :root {
    --orange: #FF9900;
    --accent: #F7991E;
    --charcoal: #333235;
    --ink: #2b2b2b;
    --paper: #ffffff;
    --backdrop: #5a5a5a;
  }
  * { margin: 0; padding: 0; box-sizing: border-box; }
  html, body {
    width: 1200px; height: 1000px; overflow: hidden;
    background: var(--backdrop);
    font-family: "Open Sans", sans-serif;
    color: var(--ink);
  }
  .card {
    position: absolute;
    width: 542px; height: 316px;
    background: var(--paper);
    box-shadow: 0 2px 6px rgba(0,0,0,.35);
    overflow: hidden;
  }
  .card-front { left: 229px; top: 170px; }
  .card-back  { left: 392px; top: 517px; }

  .wordmark {
    font-family: "Open Sans", sans-serif;
    font-weight: 800;
    color: var(--charcoal);
    line-height: 1;
    letter-spacing: -0.5px;
  }
  .card-front .wordmark {
    position: absolute; left: 25px; top: 42px;
    font-size: 25px;
  }
  .card-back .wordmark {
    position: absolute; left: 0; right: 0; top: 122px;
    text-align: center;
    font-size: 34px;
  }
  .wordmark span { display: block; }

  .person-name {
    position: absolute; left: 25px; top: 124px;
    font-family: "Orbitron", sans-serif;
    font-weight: 500;
    font-size: 13px;
    letter-spacing: 3px;
    color: var(--accent);
  }
  .person-role {
    position: absolute; left: 25px; top: 139px;
    font-size: 9px;
    color: var(--ink);
  }

  .contact-list { position: absolute; left: 24px; top: 179px; list-style: none; }
  .contact-list li {
    display: flex; align-items: center;
    height: 22.5px;
    font-size: 11px;
  }
  .contact-list svg { width: 20px; height: 20px; margin-right: 8px; flex: none; }

  .address {
    position: absolute; left: 392px; top: 233px;
    font-size: 9px; line-height: 13px;
  }

  .band { position: absolute; left: 0; bottom: 0; width: 542px; height: 16px; }

  .site-url {
    position: absolute; left: 0; right: 0; top: 254px;
    text-align: center;
    font-size: 17px;
    letter-spacing: 5px;
    color: var(--ink);
  }
</style>
</head>
<body>

<section class="card card-front">
  <div class="wordmark"><span>NORTHFIELD</span><span>BUILDERS GUILD</span></div>

  <div class="person-name">DANIEL HARTWELL</div>
  <div class="person-role">CEO/Managing Director</div>

  <ul class="contact-list">
    <li>
      <svg viewBox="0 0 20 20" aria-hidden="true"><circle cx="10" cy="10" r="9" fill="none" stroke="var(--accent)" stroke-width="1.2"/><rect x="7" y="5" width="6" height="10" rx="1" fill="none" stroke="var(--accent)" stroke-width="1.1"/><circle cx="10" cy="13.3" r=".6" fill="var(--accent)"/></svg>
      555-014-2290
    </li>
    <li>
      <svg viewBox="0 0 20 20" aria-hidden="true"><circle cx="10" cy="10" r="9" fill="none" stroke="var(--accent)" stroke-width="1.2"/><path d="M5 10 L10 5.5 L15 10 L13.6 10 L13.6 14 L6.4 14 L6.4 10 Z" fill="var(--accent)"/></svg>
      555-014-2290
    </li>
    <li>
      <svg viewBox="0 0 20 20" aria-hidden="true"><circle cx="10" cy="10" r="9" fill="none" stroke="var(--accent)" stroke-width="1.2"/><rect x="5.5" y="7" width="9" height="6.5" fill="var(--accent)"/><path d="M5.5 7 L10 10.5 L14.5 7" fill="none" stroke="#fff" stroke-width=".8"/></svg>
      dhartwell@brickwayguildnetwork.org
    </li>
    <li>
      <svg viewBox="0 0 20 20" aria-hidden="true"><circle cx="10" cy="10" r="9" fill="none" stroke="var(--accent)" stroke-width="1.2"/><circle cx="10" cy="10" r="5.5" fill="none" stroke="var(--accent)" stroke-width=".8"/><ellipse cx="10" cy="10" rx="2.4" ry="5.5" fill="none" stroke="var(--accent)" stroke-width=".8"/><path d="M4.5 10 H15.5 M5.3 7.3 H14.7 M5.3 12.7 H14.7" stroke="var(--accent)" stroke-width=".7"/></svg>
      www.brickwayguildnetwork.org
    </li>
  </ul>

  <div class="address">118 Alder Street NW Suite<br>210 Lakeview Mi 49310</div>

  <svg class="band" viewBox="0 0 542 16" preserveAspectRatio="none" aria-hidden="true">
    <polygon points="0,0 276,0 263,16 0,16" fill="var(--charcoal)"/>
    <polygon points="282,0 542,0 542,16 269,16" fill="var(--accent)"/>
  </svg>
</section>

<section class="card card-back">
  <div class="wordmark"><span>NORTHFIELD</span><span>BUILDERS GUILD</span></div>
  <div class="site-url">www.brickwayguildnetwork.org</div>
</section>

</body>
</html>
```